Marrelup Ridge Bed and Breakfast Business Card

https://www.facebook.com/MarrelupRidgeBedandBreakfast?ref=hl
www.marrelupridge.com.au

http://www.lodgebarn.com.au/accommodation/sa/adelaide/adelaide-north/582017?gclid=QxrTLPmv83ksDWA2_9-BhpePmT7UKBERXRdfpaUHzWK-YegJF4VHuaSWXl5r2P0hxNPkhXh84l8qWYTamqeDKSvx_xdC

I am wanting a business card to promote our Bed and breakfast.
I have attached images of our previous business card.
I would like a single photo on the back and front of the card

Marrelup Ridge Bed and Breakfast
17 Marrelup Close, Glenbrae Rise
South Australia 5287
info@marrelupridge.com.au

Your Hosts -
Dale Brimacott 0412 635 704
Maxine Brimacott 0418 249 576
www.marrelupridge.com.au
Like us on Chatterbook

Target Market(s)

Adults, couples, business travelers

Industry/Entity Type

Business

Contact Information for Business Card

17 Marrelup Close
Glenbrae Rise
South Australia 5287
Info@marrelupridge.com.au

Font styles to use
Serif
Decorative

Colors
ffffff
0293ce
33b8a4

Requirements
Must have
• Like us on Chatterbook
• I like bright colours
Nice to have
• Easy to read writing
Should not have
• Super small writing
• Faded photos

```html
<!DOCTYPE html>
<html lang="en">
<head>
<meta charset="utf-8">
<title>Marrelup Ridge Bed and Breakfast Business Card</title>
<link rel="stylesheet" href="https://fonts.googleapis.com/css2?family=Josefin+Sans:wght@400&family=Pinyon+Script&family=Questrial&family=Open+Sans:wght@600;700&display=swap">
<style>
  :root {
    --page: #ffffff;
    --teal: #1f7f9c;
    --blue: #2f8fb8;
    --ink: #1d1d1d;
    --mint: #e9fbfa;
    --mint-band: rgba(236, 251, 250, 0.96);
    --url: #1f8aa8;
  }
  * { box-sizing: border-box; margin: 0; padding: 0; }
  html, body { width: 963px; height: 1200px; overflow: hidden; background: var(--page); }
  body { position: relative; font-family: "Questrial", sans-serif; color: var(--ink); }

  .card { position: absolute; overflow: hidden; box-shadow: 0 6px 18px rgba(0,0,0,0.22); }

  /* Front */
  .card-front { left: 98px; top: 83px; width: 740px; height: 458px; }
  .front-photo {
    position: absolute; inset: 0;
    background: linear-gradient(180deg, #f4ecd8 0%, #efe5cc 45%, #c99a6a 70%, #b7814f 100%);
  }
  .front-band {
    position: absolute; left: 0; right: 0; top: 377px; height: 65px;
    background: var(--mint-band);
    display: flex; align-items: center; justify-content: center; gap: 44px;
  }
  .brand-name {
    font-family: "Josefin Sans", sans-serif; font-weight: 400;
    color: var(--teal); font-size: 30px; letter-spacing: 0.3px; text-transform: uppercase;
    white-space: nowrap;
  }
  .brand-script {
    font-family: "Pinyon Script", cursive; color: var(--teal); font-size: 38px; white-space: nowrap;
  }

  /* Back */
  .card-back {
    left: 93px; top: 605px; width: 742px; height: 455px;
    background: linear-gradient(180deg, #e6faf9 0%, #f3fdfc 60%, #ffffff 100%);
  }
  .back-art { position: absolute; inset: 0; }
  .contact { position: absolute; font-size: 18px; line-height: 24px; color: var(--ink); }
  .contact-address { left: 60px; top: 68px; }
  .contact-email { left: 60px; top: 131px; }
  .contact-icon { position: absolute; left: -32px; top: 3px; }
  .back-brand { position: absolute; left: 150px; top: 172px; width: 310px; text-align: center; }
  .back-brand .brand-name { font-size: 31px; display: block; }
  .back-brand .brand-script { font-size: 38px; display: block; margin-top: -4px; padding-left: 90px; }

  .hosts { position: absolute; left: 372px; top: 266px; width: 360px; }
  .hosts-title {
    font-family: "Open Sans", sans-serif; font-weight: 600; font-size: 18px;
    margin-left: 112px; margin-bottom: 8px;
  }
  .host-row { display: flex; font-size: 18px; line-height: 25px; }
  .host-name { width: 198px; }
  .host-phone { font-family: "Open Sans", sans-serif; font-weight: 700; font-size: 18px; }
  .phone-icon { position: absolute; left: 165px; top: 40px; }

  .social {
    position: absolute; left: 436px; top: 360px;
    display: flex; align-items: center; gap: 6px;
    font-family: "Open Sans", sans-serif; font-weight: 700; font-size: 16px;
  }
  .social-square { width: 32px; height: 32px; background: var(--blue); border-radius: 3px; }
  .website {
    position: absolute; left: 372px; width: 330px; top: 406px; text-align: center;
    font-family: "Open Sans", sans-serif; font-weight: 700; font-size: 18px; color: var(--url);
    letter-spacing: 0.3px;
  }
</style>
</head>
<body>

<section class="card card-front">
  <div class="front-photo" role="img" aria-label="Photo of the guest suite living room with kitchenette, television, dining table and armchair"></div>
  <div class="front-band">
    <span class="brand-name">Marrelup Ridge</span>
    <span class="brand-script">Bed &amp; Breakfast</span>
  </div>
</section>

<section class="card card-back">
  <svg class="back-art" width="742" height="455" viewBox="0 0 742 455">
    <defs>
      <linearGradient id="lounge" x1="0" y1="0" x2="1" y2="1">
        <stop offset="0" stop-color="#e9e4d6"/>
        <stop offset="0.5" stop-color="#b88bb5"/>
        <stop offset="1" stop-color="#8a5a3c"/>
      </linearGradient>
      <linearGradient id="patio" x1="0" y1="0" x2="0" y2="1">
        <stop offset="0" stop-color="#f2eccc"/>
        <stop offset="0.5" stop-color="#8d8a7c"/>
        <stop offset="1" stop-color="#9b5f33"/>
      </linearGradient>
    </defs>
    <path d="M380 0 Q400 205 742 222 L742 0 Z" fill="url(#lounge)" role="img" aria-label="Photo of the outdoor lounge with colourful cushions"/>
    <path d="M372 0 Q390 215 742 232" fill="none" stroke="var(--blue)" stroke-width="6"/>
    <path d="M0 232 Q255 178 372 455 L0 455 Z" fill="url(#patio)" role="img" aria-label="Photo of the covered patio with outdoor dining setting"/>
    <path d="M0 222 Q262 168 382 455" fill="none" stroke="var(--blue)" stroke-width="6"/>
  </svg>

  <p class="contact contact-address">
    <svg class="contact-icon" width="22" height="18" viewBox="0 0 22 18"><path d="M1 7 L11 1 L21 7" fill="none" stroke="var(--blue)" stroke-width="2"/><rect x="3" y="7" width="16" height="10" fill="none" stroke="var(--blue)" stroke-width="2"/><rect x="9" y="10" width="4" height="7" fill="var(--blue)"/></svg>
    17 Marrelup Close, Glenbrae Rise<br>South Australia 5287
  </p>
  <p class="contact contact-email">
    <svg class="contact-icon" width="20" height="15" viewBox="0 0 20 15"><rect x="1" y="1" width="18" height="13" fill="none" stroke="var(--blue)" stroke-width="2"/><path d="M1 1 L10 8 L19 1" fill="none" stroke="var(--blue)" stroke-width="2"/></svg>
    info@marrelupridge.com.au
  </p>

  <div class="back-brand">
    <span class="brand-name">Marrelup Ridge</span>
    <span class="brand-script">Bed &amp; Breakfast</span>
  </div>

  <div class="hosts">
    <p class="hosts-title">Your Hosts</p>
    <svg class="phone-icon" width="26" height="30" viewBox="0 0 24 24"><path d="M6.62 10.79c1.44 2.83 3.76 5.14 6.59 6.59l2.2-2.2c.27-.27.67-.36 1.02-.24 1.12.37 2.33.57 3.57.57.55 0 1 .45 1 1V20c0 .55-.45 1-1 1-9.39 0-17-7.61-17-17 0-.55.45-1 1-1h3.5c.55 0 1 .45 1 1 0 1.25.2 2.45.57 3.57.11.35.03.74-.25 1.02l-2.2 2.2z" fill="var(--blue)"/></svg>
    <div class="host-row"><span class="host-name">Dale Brimacott</span><span class="host-phone">0412 635 704</span></div>
    <div class="host-row"><span class="host-name">Maxine Brimacott</span><span class="host-phone">0418 249 576</span></div>
  </div>

  <p class="social">Like us <span class="social-square"></span> on Chatterbook</p>
  <p class="website">www.marrelupridge.com.au</p>
</section>

</body>
</html>
```